Pedal Wardens stationary
business card, letter head, powerpoint template
Creative Brief
Use same font as used in my logo
Tomas Lindqvo
Owner & Managing Director
Ekbackevägen 14 17452 Sundbyö
tomas@pedalwardens.cc
www.pedalwardens.cc
org.nr. 558213-4406
Business card and stationary design. We provide umpires & referees for teams/organizations.

```html
<!DOCTYPE html>
<html lang="en">
<head>
<meta charset="utf-8">
<title>Pedal Wardens – Business Card</title>
<link rel="stylesheet" href="https://fonts.googleapis.com/css2?family=Raleway:wght@300;400&family=Open+Sans:wght@400;600;700&display=swap">
<style>
  :root {
    --backdrop: #d9d9d9;
    --card: #ffffff;
    --ink: #2e2e2e;
    --ink-soft: #555555;
    --band-dark: #3a3a3a;
    --band-mid: #5a5a5a;
  }
  * { margin: 0; padding: 0; box-sizing: border-box; }
  html, body { width: 1200px; height: 987px; overflow: hidden; }
  body {
    background: var(--backdrop);
    font-family: "Open Sans", Arial, sans-serif;
    color: var(--ink);
    position: relative;
  }
  .card {
    position: absolute;
    left: 280px;
    width: 640px;
    height: 380px;
    background: var(--card);
    border-radius: 22px;
    overflow: hidden;
    box-shadow: 0 6px 18px rgba(0,0,0,0.18);
  }
  .card--back { top: 80px; }
  .card--front { top: 527px; }

  /* Back */
  .back-mark {
    position: absolute;
    left: 50%;
    top: 96px;
    transform: translateX(-50%);
    width: 124px;
    height: 124px;
    border-radius: 50%;
    background: var(--ink);
  }
  .back-url {
    position: absolute;
    left: 0; right: 0;
    top: 262px;
    text-align: center;
    font-family: "Raleway", Arial, sans-serif;
    font-size: 17px;
    letter-spacing: 7px;
    color: var(--ink);
  }

  /* Front */
  .brand {
    position: absolute;
    left: 0; right: 0;
    top: 26px;
    text-align: center;
  }
  .brand-mark {
    width: 68px;
    height: 68px;
    border-radius: 50%;
    background: var(--ink);
    margin: 0 auto 14px;
  }
  .brand-name {
    font-family: "Raleway", Arial, sans-serif;
    font-weight: 300;
    font-size: 30px;
    letter-spacing: 9px;
    color: var(--ink);
  }
  .details {
    position: absolute;
    top: 176px;
    left: 0; right: 0;
    display: flex;
    justify-content: center;
    align-items: center;
  }
  .person {
    text-align: right;
    padding-right: 18px;
  }
  .person-name { font-weight: 700; font-size: 16px; }
  .person-role { font-size: 13px; color: var(--ink-soft); margin-top: 2px; }
  .divider {
    width: 1px;
    height: 82px;
    background: var(--ink);
  }
  .contacts {
    list-style: none;
    padding-left: 16px;
    font-size: 12.5px;
    line-height: 20px;
    color: var(--ink);
  }
  .contacts li { display: flex; align-items: center; gap: 8px; }
  .contact-icon {
    width: 14px; height: 14px;
    border-radius: 50%;
    background: var(--ink);
    display: inline-flex;
    align-items: center;
    justify-content: center;
    flex: none;
  }
  .wave { position: absolute; left: 0; bottom: 0; width: 640px; height: 380px; }
</style>
</head>
<body>

  <section class="card card--back">
    <div class="back-mark" aria-hidden="true"></div>
    <p class="back-url">www.pedalwardens.cc</p>
  </section>

  <section class="card card--front">
    <svg class="wave" viewBox="0 0 640 380" aria-hidden="true">
      <path d="M0 300 C160 250 300 345 640 292 L640 380 L0 380 Z" fill="var(--band-mid)"/>
      <path d="M0 306 C160 258 300 352 640 300 L640 316 C300 365 160 280 0 330 Z" fill="var(--card)"/>
      <path d="M0 336 C170 292 320 378 640 326 L640 380 L0 380 Z" fill="var(--band-dark)"/>
    </svg>

    <header class="brand">
      <div class="brand-mark" aria-hidden="true"></div>
      <h1 class="brand-name">PEDAL WARDENS</h1>
    </header>

    <div class="details">
      <div class="person">
        <p class="person-name">Tomas Lindqvo</p>
        <p class="person-role">Owner &amp; Managing Director</p>
      </div>
      <div class="divider"></div>
      <ul class="contacts">
        <li>
          <span class="contact-icon"><svg width="8" height="10" viewBox="0 0 8 10"><path d="M4 0 C1.8 0 0 1.7 0 3.8 C0 6.5 4 10 4 10 C4 10 8 6.5 8 3.8 C8 1.7 6.2 0 4 0 Z" fill="#fff"/><circle cx="4" cy="3.8" r="1.4" fill="#2e2e2e"/></svg></span>
          Ekbackevägen 14 17452 Sundbyö
        </li>
        <li>
          <span class="contact-icon"><svg width="9" height="7" viewBox="0 0 9 7"><rect x="0.5" y="0.5" width="8" height="6" fill="none" stroke="#fff"/><path d="M0.5 0.5 L4.5 4 L8.5 0.5" fill="none" stroke="#fff"/></svg></span>
          tomas@pedalwardens.cc
        </li>
        <li>
          <span class="contact-icon"><svg width="9" height="9" viewBox="0 0 10 10"><circle cx="5" cy="5" r="4.3" fill="none" stroke="#fff"/><path d="M0.7 5 H9.3 M5 0.7 C2.8 3 2.8 7 5 9.3 M5 0.7 C7.2 3 7.2 7 5 9.3" fill="none" stroke="#fff" stroke-width="0.8"/></svg></span>
          www.pedalwardens.cc
        </li>
      </ul>
    </div>
  </section>

</body>
</html>
```